Stationary Design for Stunning new Logo

I need to envelopes, letterhead, business cards designed to compliment our new logo.

We are a 25 year old printing company going through a brand refresh. All items should have the design extended to both sides for full print ability.

Industry/Entity Type

Printing

Requirements
Must have
• It must utilize the new logo & colors PMS 300 & PMS 295.

```html
<!DOCTYPE html>
<html lang="en">
<head>
<meta charset="utf-8">
<title>Novapress Business Card</title>
<link rel="stylesheet" href="https://fonts.googleapis.com/css2?family=Open+Sans:wght@400;600;700;800&display=swap">
<style>
  :root {
    --pms-300: #0069b4;
    --pms-295: #0a3d73;
    --paper: #ffffff;
    --stage: #eceef1;
    --ink-light: #ffffff;
    --shadow: rgba(10, 30, 60, 0.18);
  }
  * { box-sizing: border-box; margin: 0; padding: 0; }
  html, body { width: 1200px; height: 720px; overflow: hidden; }
  body {
    background: var(--stage);
    font-family: "Open Sans", Arial, sans-serif;
    position: relative;
  }
  .card {
    position: absolute;
    width: 540px;
    height: 309px;
    border-radius: 4px;
    overflow: hidden;
    box-shadow: 0 10px 30px var(--shadow);
  }
  .card--front { left: 40px; top: 205px; background: var(--paper); }
  .card--back { left: 620px; top: 205px; background: var(--pms-295); }

  .card__waves { position: absolute; inset: 0; width: 100%; height: 100%; }

  .brand { position: absolute; left: 28px; top: 72px; }
  .brand__row { display: flex; align-items: center; gap: 8px; }
  .brand__dot {
    width: 28px; height: 28px; border-radius: 50%;
    background: var(--pms-300);
  }
  .brand__name {
    font-weight: 800; font-size: 34px; letter-spacing: 1px;
    color: var(--pms-300); line-height: 1;
  }
  .brand__tagline {
    margin-top: 4px; margin-left: 36px;
    font-size: 7px; font-weight: 600; letter-spacing: 0.3px;
    color: var(--pms-300); text-transform: uppercase; white-space: nowrap;
  }

  .holder { position: absolute; left: 62px; top: 196px; }
  .holder__name { font-size: 17px; font-weight: 700; color: var(--pms-295); }
  .holder__title { font-size: 13px; font-weight: 600; color: var(--pms-300); }

  .contact {
    position: absolute; left: 392px; top: 80px;
    list-style: none; color: var(--ink-light); font-size: 11.5px;
  }
  .contact__item { display: flex; align-items: center; gap: 7px; line-height: 20px; white-space: nowrap; }
  .contact__icon { width: 11px; height: 11px; flex: none; }
  .address {
    position: absolute; right: 20px; top: 190px;
    color: var(--ink-light); font-size: 11px; white-space: nowrap;
  }

  .back__mark {
    position: absolute; left: 50%; top: 62px; transform: translateX(-50%);
    width: 120px; height: 120px; border-radius: 50%;
    border: 10px solid var(--ink-light);
  }
  .back__url {
    position: absolute; left: 0; right: 0; top: 226px; text-align: center;
    color: var(--ink-light); font-size: 16px; letter-spacing: 3px;
  }
</style>
</head>
<body>
  <section class="card card--front" aria-label="Business card front">
    <svg class="card__waves" viewBox="0 0 540 309" preserveAspectRatio="none" aria-hidden="true">
      <path d="M540,18 C440,18 360,30 320,110 C285,180 230,240 0,250 L0,309 L540,309 Z" fill="var(--pms-295)"/>
      <path d="M540,18 C440,18 360,30 320,110 C285,180 230,240 0,250 L0,309 L540,309 Z" fill="var(--paper)" transform="translate(0,12)"/>
      <path d="M540,18 C440,18 360,30 320,110 C285,180 230,240 0,250 L0,309 L540,309 Z" fill="var(--pms-300)" transform="translate(0,18)"/>
      <path d="M0,290 C170,292 270,280 320,256 C280,292 170,304 0,302 Z" fill="var(--pms-295)" opacity="0.55"/>
    </svg>

    <div class="brand">
      <div class="brand__row">
        <span class="brand__dot"></span>
        <span class="brand__name">NOVAPRESS</span>
      </div>
      <p class="brand__tagline">Outstanding service • Quality product • Competitive pricing.</p>
    </div>

    <div class="holder">
      <p class="holder__name">Your Name</p>
      <p class="holder__title">Title</p>
    </div>

    <ul class="contact">
      <li class="contact__item">
        <svg class="contact__icon" viewBox="0 0 12 12"><circle cx="6" cy="6" r="5.3" fill="none" stroke="#fff" stroke-width="1.2"/><path d="M4,3.5 L5,3.5 L5.5,5 L4.8,5.5 Q5.5,7 6.8,7.4 L7.3,6.7 L8.6,7.2 L8.6,8.3 Q5,8.6 3.6,4.2 Z" fill="#fff"/></svg>
        555-010-2040
      </li>
      <li class="contact__item">
        <svg class="contact__icon" viewBox="0 0 12 12"><circle cx="6" cy="3.6" r="2.4" fill="#fff"/><path d="M1.5,11 Q1.5,6.6 6,6.6 Q10.5,6.6 10.5,11 Z" fill="#fff"/></svg>
        555-010-3050
      </li>
      <li class="contact__item">
        <svg class="contact__icon" viewBox="0 0 12 12"><rect x="1" y="2.5" width="10" height="7" rx="1" fill="#fff"/><path d="M1.5,3 L6,6.6 L10.5,3" fill="none" stroke="var(--pms-300)" stroke-width="1"/></svg>
        hello@novapress.com
      </li>
      <li class="contact__item">
        <svg class="contact__icon" viewBox="0 0 12 12"><circle cx="6" cy="6" r="5.2" fill="none" stroke="#fff" stroke-width="1.1"/><ellipse cx="6" cy="6" rx="2.2" ry="5.2" fill="none" stroke="#fff" stroke-width="0.9"/><path d="M0.8,6 H11.2" stroke="#fff" stroke-width="0.9"/></svg>
        www.novapress.com
      </li>
    </ul>
    <p class="address">Street Name, City Name, Zip Code 00423</p>
  </section>

  <section class="card card--back" aria-label="Business card back">
    <span class="back__mark"></span>
    <p class="back__url">www.novapress.com</p>
  </section>
</body>
</html>
```